Electrical contracting business specialising in smoke detector installation needs flyer design

i need a flyer design made up highlighting the fact that the Qld legislation is changing on smoke detectors in homes for everyones safety. I am an electrical contractor ( Tallow Bend Electrical) specialising in smoke detector installation to comply with the new Qld legislation. Some of the wording that can be used-
When you sleep, your sense of smell also sleeps. If a fire starts, toxic fumes canovercome you. Photoelectric smoke alarms see smoke and will alert you early, so you can escape. With interconnected alarms, you will be alerted no matter where you are, or where the fire starts.
New legislation specifies the type, positioning and interconnectedness of alarms, which are critical factors for an early warning and a quick escape.
To give your family the best chance of surviving a house fire, update your smoke alarms to match the new legislation as soon as you can. Call us on 0471385269

Target Market(s)

Body Corporates , people selling and renting their properties

Industry/Entity Type

Electrician

Colors

Designer to choose colors to be used in the design.

Requirements
Must have
• Safety aspect.

```html
<!DOCTYPE html>
<html lang="en">
<head>
<meta charset="utf-8">
<title>Smoke Alarm Legislation Flyer</title>
<link rel="stylesheet" href="https://fonts.googleapis.com/css2?family=Lato:wght@400;700;900&display=swap">
<style>
  :root {
    --stage: #17181c;
    --ink: #0a0a0a;
    --paper: #ffffff;
    --gold: #c4944f;
    --gold-deep: #a8793a;
    --scene-dark: #1c2430;
    --scene-light: #4f6a80;
  }
  * { margin: 0; padding: 0; box-sizing: border-box; }
  html, body { width: 1200px; height: 848px; overflow: hidden; background: var(--stage); }
  .canvas { position: relative; width: 1200px; height: 848px; }
  .flyer {
    position: absolute; left: 320px; top: 28px;
    width: 560px; height: 792px; background: var(--ink);
    font-family: "Lato", sans-serif; overflow: hidden;
  }
  .flyer-shapes { position: absolute; inset: 0; }
  .headline {
    position: absolute; left: 0; right: 0; top: 26px; text-align: center;
    font-weight: 900; text-transform: uppercase; line-height: 1;
  }
  .headline-main { display: block; color: var(--gold); font-size: 50px; letter-spacing: 1px; }
  .headline-sub { display: block; color: var(--ink); font-size: 27px; margin-top: 6px; }
  .intro {
    position: absolute; left: 40px; right: 40px; top: 116px;
    font-size: 11.5px; line-height: 1.35; color: var(--ink); text-align: center; font-weight: 700;
  }
  .brand {
    position: absolute; left: 34px; top: 440px; width: 200px;
    color: var(--gold); font-weight: 400; font-size: 30px; line-height: 1.1;
  }
  .legislation {
    position: absolute; left: 270px; right: 26px; top: 520px;
    color: var(--paper); font-weight: 700; font-size: 15px; line-height: 1.3; text-align: center;
  }
  .call-note {
    position: absolute; left: 40px; right: 40px; top: 664px;
    color: var(--ink); font-weight: 700; font-size: 13px; line-height: 1.3; text-align: center;
  }
  .call-line {
    position: absolute; left: 0; right: 0; top: 716px; text-align: center;
    color: var(--ink); font-weight: 900; font-size: 42px; letter-spacing: 0.5px; white-space: nowrap;
  }
</style>
</head>
<body>
<div class="canvas">
  <article class="flyer">
    <svg class="flyer-shapes" width="560" height="792" viewBox="0 0 560 792">
      <defs>
        <linearGradient id="sceneTone" x1="0" y1="0" x2="1" y2="1">
          <stop offset="0" stop-color="#1c2430"/>
          <stop offset="0.55" stop-color="#4f6a80"/>
          <stop offset="1" stop-color="#1c2430"/>
        </linearGradient>
      </defs>
      <path role="img" aria-label="Illustration of a home at night with interconnected photoelectric smoke alarms casting blue detection cones as a fire starts in a bedroom"
            d="M0 130 Q330 180 560 218 V510 Q260 385 0 385 Z" fill="url(#sceneTone)"/>
      <path class="top-panel" d="M0 0 H560 V210 Q330 172 0 150 Z" fill="var(--paper)"/>
      <path class="top-rule" d="M0 152 Q330 174 560 212" fill="none" stroke="var(--gold)" stroke-width="9"/>
      <path class="lower-panel" d="M0 380 Q260 380 560 500 V792 H0 Z" fill="var(--ink)"/>
      <path class="lower-rule" d="M0 382 Q260 382 560 502" fill="none" stroke="var(--gold)" stroke-width="8"/>
      <path class="call-panel" d="M0 600 Q320 606 560 652 V792 H0 Z" fill="var(--gold)"/>
    </svg>

    <h1 class="headline">
      <span class="headline-main">When you sleep</span>
      <span class="headline-sub">Your sense of smell also sleeps.</span>
    </h1>
    <p class="intro">If a fire starts, toxic fumes canovercome you. Photoelectric smoke alarms see smoke and will alert you early, so you can escape. With interconnected alarms, you will be alerted no matter where you are, or where the fire starts.</p>

    <div class="brand">Tallow Bend Electrical</div>

    <p class="legislation">New legislation specifies the type, positioning and interconnectedness of alarms, which are critical factors for an early warning and a quick escape.</p>

    <p class="call-note">To give your family the best chance of surviving a house fire, update your smoke alarms to match the new legislation as soon as you can.</p>
    <p class="call-line">Call us on 0471385269</p>
  </article>
</div>
</body>
</html>
```